Talvern Risk Management - Bridgewell Ledger

Upgrade existing PP per the upload. I will use this to email to Prospects and clients as well as posting to our website.
Edit and update pages - this PP was created several years ago and needs a full update based on the same content. Better graphics etc etc are needed
Create some links to websites
Talvern Risk Management is a professional consultant where owners have MBA's. Law Degrees and CPCU Designation. PP should be designed with this in mind similar to resources used by CPA's, Accountants or Financial Advisors
Updates
Need extra days to review
Target Market(s)
Construction Contractors
Colors
Designer to choose colors to be used in the design.
Requirements
Must have
- Follow existing PP
Nice to have
- Take a look at our current website which will be upgraded when PP is complete
- www.harrowquillpeak.biz

```html
<!DOCTYPE html>
<html lang="en">
<head>
<meta charset="utf-8">
<title>Keystone Build Advisors – Presentation</title>
<link href="https://fonts.googleapis.com/css2?family=Open+Sans:wght@400;600;700&family=Raleway:wght@700&display=swap" rel="stylesheet">
<style>
  :root{
    --slate:#333d48;
    --slate-deep:#27313c;
    --red:#d71920;
    --ink:#1e1e1e;
    --muted:#6b6b6b;
    --rule:#e6e6e6;
    --paper:#ffffff;
  }
  *{margin:0;padding:0;box-sizing:border-box}
  html,body{width:800px;height:1200px;overflow:hidden;background:var(--paper)}
  body{position:relative;font-family:"Open Sans",sans-serif;color:var(--ink)}
  .slide{position:absolute;left:148px;width:504px;height:284px;background:var(--paper);
    box-shadow:0 2px 6px rgba(0,0,0,.28);overflow:hidden}
  .s1{top:8px}.s2{top:308px}.s3{top:608px}.s4{top:908px}

  /* cover */
  .cover-photo{position:absolute;inset:0;
    background:linear-gradient(180deg,#34414f 0%,#3c4a58 45%,#4a5560 75%,#5a6258 100%)}
  .cover-title{position:absolute;top:104px;width:100%;text-align:center;color:#fff;
    font-family:"Raleway",sans-serif;font-weight:700;font-size:27px}
  .cover-sub{position:absolute;top:138px;width:100%;text-align:center;color:#fff;font-size:12.6px}
  .cover-rule{position:absolute;top:165px;left:237px;width:30px;height:2px;background:var(--red)}
  .cover-url{position:absolute;top:229px;width:100%;text-align:center;color:var(--red);
    font-size:8px;text-decoration:underline}

  /* content slides */
  .slide-title{position:absolute;left:25px;top:20px;font-size:19px;font-weight:400}
  .title-mark{position:absolute;left:25px;top:45px;width:30px;height:2px;background:var(--red)}
  .title-rule{position:absolute;left:0;right:0;top:49px;height:1px;background:var(--rule)}

  .footer{position:absolute;left:0;bottom:0;width:504px;height:15px;background:var(--slate)}
  .footer-copy{position:absolute;left:7px;top:4px;font-size:5px;color:#fff}
  .footer-page{position:absolute;right:18px;top:0;width:18px;height:15px;background:#fff;
    font-size:6px;color:#999;text-align:center;line-height:15px}
  .footer-flag{position:absolute;right:0;top:0;width:18px;height:15px;background:var(--red)}

  .mission{position:absolute;left:25px;top:76px;width:440px;list-style:none}
  .mission li{position:relative;padding-left:9px;font-size:12.6px;line-height:16.2px;margin-bottom:4.8px}
  .mission li::before{content:"•";position:absolute;left:0;top:0;color:var(--red)}

  .team-photo{position:absolute;left:0;top:66px;width:214px;height:168px;
    background:linear-gradient(135deg,#c9d2dc 0%,#8896a6 45%,#2e3a55 100%)}
  .philosophy{position:absolute;left:214px;top:66px;width:290px;height:168px;background:var(--slate)}
  .philosophy p{position:absolute;left:28px;top:25px;width:228px;color:#fff;font-size:9.1px;line-height:11.4px}

  .goals-photo{position:absolute;left:0;top:66px;width:504px;height:112px;
    background:linear-gradient(180deg,#3f4853 0%,#59626c 60%,#6e757d 100%)}
  .goal{position:absolute;top:149px;width:110px;margin-left:-55px;text-align:center}
  .goal svg{display:block;margin:0 auto}
  .goal p{margin-top:6px;font-size:6.2px;line-height:8px;font-weight:700;color:var(--muted)}
</style>
</head>
<body>

<section class="slide s1">
  <div class="cover-photo" role="img" aria-label="Construction site with tower cranes at dusk, dark blue overlay"></div>
  <h1 class="cover-title">Keystone Build Advisors</h1>
  <p class="cover-sub">Management Consultants for the Construction Industry</p>
  <div class="cover-rule"></div>
  <a class="cover-url">www.harrowquillpeak.biz</a>
</section>

<section class="slide s2">
  <h2 class="slide-title">Mission Statement</h2>
  <div class="title-mark"></div><div class="title-rule"></div>
  <ul class="mission">
    <li>To provide the highest level of personal financial services in a friendly, professional manner</li>
    <li>To encourage contractor clients to establish and extend effective management systems in their companies</li>
    <li>To increase the knowledge and ability of our clients to manage and control their financial well-being</li>
    <li>To provide sound financial/operating management advice in order to maximize clients corporate value while minimizing risk</li>
  </ul>
  <footer class="footer"><span class="footer-copy">© 2018 Keystone Build Advisors. All rights reserved.</span><span class="footer-page">2</span><span class="footer-flag"></span></footer>
</section>

<section class="slide s3">
  <h2 class="slide-title">Keystone Build Advisors Philosophy</h2>
  <div class="title-mark"></div><div class="title-rule"></div>
  <div class="team-photo" role="img" aria-label="Three businessmen in suits wearing yellow hard hats"></div>
  <div class="philosophy">
    <p>Keystone Build Advisors is dedicated to the safe and successful growth of their construction clients by strategically implementing comprehensive and practical management systems. KBA will minimize business risk by maximizing critical information flows to the CEO. Throughout the organization, KBA will provide the Client CEO with the necessary tools for the critical information needed to manage his growing company. The objective is to maximize company value and minimize business risk</p>
  </div>
  <footer class="footer"><span class="footer-copy">© 2018 Keystone Build Advisors. All rights reserved.</span><span class="footer-page">3</span><span class="footer-flag"></span></footer>
</section>

<section class="slide s4">
  <h2 class="slide-title">Goals and Objectives</h2>
  <div class="title-mark"></div><div class="title-rule"></div>
  <div class="goals-photo" role="img" aria-label="Muted photo of a hard hat and plans on a desk"></div>

  <div class="goal" style="left:53px">
    <svg width="56" height="56" viewBox="0 0 56 56"><circle cx="28" cy="28" r="27" fill="var(--red)" stroke="#fff" stroke-width="1.5"/>
      <g fill="none" stroke="#fff" stroke-width="1.2"><circle cx="24" cy="30" r="6"/><circle cx="24" cy="30" r="2"/><circle cx="34" cy="22" r="4"/><circle cx="34" cy="22" r="1.3"/><path d="M24 21v3M24 36v3M15 30h3M30 30h3M34 16v2M34 26v2M28 22h2M38 22h2"/></g></svg>
    <p>Review Why<br>Contractors Fail</p>
  </div>
  <div class="goal" style="left:144px">
    <svg width="56" height="56" viewBox="0 0 56 56"><circle cx="28" cy="28" r="27" fill="var(--red)" stroke="#fff" stroke-width="1.5"/>
      <g fill="none" stroke="#fff" stroke-width="1.2"><circle cx="32" cy="26" r="4"/><path d="M24 40v-4a8 8 0 0 1 16 0v4"/><circle cx="21" cy="21" r="4"/><circle cx="21" cy="21" r="1.3"/><path d="M21 15v2M21 25v2M15 21h2M25 21h1"/></g></svg>
    <p>Focus on Why Contractors<br>Succeed</p>
  </div>
  <div class="goal" style="left:254px">
    <svg width="56" height="56" viewBox="0 0 56 56"><circle cx="28" cy="28" r="27" fill="var(--red)" stroke="#fff" stroke-width="1.5"/>
      <g fill="none" stroke="#fff" stroke-width="1.2"><circle cx="28" cy="18" r="4"/><circle cx="20" cy="34" r="4"/><circle cx="36" cy="34" r="4"/><path d="M26 21l-4 9M30 21l4 9M24 34h8"/><circle cx="16" cy="20" r="1.5"/><circle cx="40" cy="20" r="1.5"/></g></svg>
    <p>Establish Basic Premise -<br>Knowledge/Education/Commitment<br>to Change will bridge<br>the gap for success</p>
  </div>
  <div class="goal" style="left:362px">
    <svg width="56" height="56" viewBox="0 0 56 56"><circle cx="28" cy="28" r="27" fill="var(--red)" stroke="#fff" stroke-width="1.5"/>
      <g fill="none" stroke="#fff" stroke-width="1.2"><circle cx="28" cy="24" r="9"/><path d="M28 19l1.6 3.3 3.6.5-2.6 2.5.6 3.6-3.2-1.7-3.2 1.7.6-3.6-2.6-2.5 3.6-.5z"/><path d="M22 31l-3 9 4-2 2 3 2-7M34 31l3 9-4-2-2 3-2-7"/></g></svg>
    <p>Implement Contractors<br>Navigation System to<br>accomplish Mission<br>Statement</p>
  </div>
  <div class="goal" style="left:455px">
    <svg width="56" height="56" viewBox="0 0 56 56"><circle cx="28" cy="28" r="27" fill="var(--red)" stroke="#fff" stroke-width="1.5"/>
      <g fill="none" stroke="#fff" stroke-width="1.2"><circle cx="34" cy="30" r="6"/><circle cx="34" cy="30" r="2"/><path d="M16 24h12M16 28h9M16 32h10M28 20l6-4v3h4"/><circle cx="35" cy="17" r="2"/></g></svg>
    <p>Support Client in the<br>continuing commitment to<br>use Integrated Management<br>System put in place</p>
  </div>

  <footer class="footer"><span class="footer-copy">© 2018 Keystone Build Advisors. All rights reserved.</span><span class="footer-page">4</span><span class="footer-flag"></span></footer>
</section>

</body>
</html>
```